Plakat Ausbildung für Handwerksbetrieb
Zielgruppe
Wir sind ein Handwerksbetrieb und möchten mit einem Banner auf unsere Ausbildungsplätze hinweisen und junge Menschen (vor allem Schüler + Studenten) ansprechen. Der Banner soll nach Möglichkeit quadratisch sein. Unser bisheriges Logo habe ich als Datei angehängt. Desweiteren ein Bild wie ich es mir in etwa vorstellen würde das sich die 3 Elemente (Feuer, Wasser und Strom als Synonym für Heizung, Sanitär und Elektro) darstellen. Dazu noch eine knappe Beschreibung welche Ausbildungsplätze wir anbieten und auf unsere Homepage verweisen.
Aufgabenstellung
Ausbildungsplätze als:
- Anlagenmechaniker/in für Sanitär-, Heizungs- und Klimatechnik
- Elektroinstallateur/in (Energie- und Gebäudetechnik)

```html
<!DOCTYPE html>
<html lang="de">
<head>
<meta charset="utf-8">
<title>Ausbildungsplätze – KORVELD</title>
<link href="https://fonts.googleapis.com/css2?family=Montserrat:wght@700;800&display=swap" rel="stylesheet">
<style>
  :root {
    --backdrop: #adadad;
    --ink-white: #ffffff;
    --panel-black: #000000;
    --accent-red: #e3222b;
    --icon-yellow: #f5c518;
    --water-blue: #17355a;
    --deep-navy: #0c1a2e;
    --fire-orange: #e8561a;
    --ember-red: #6a1a12;
  }
  html, body {
    margin: 0;
    padding: 0;
    width: 1200px;
    height: 1117px;
    overflow: hidden;
    background: var(--backdrop);
    font-family: "Montserrat", Arial, sans-serif;
  }
  .poster {
    position: absolute;
    left: 135px;
    top: 94px;
    width: 930px;
    height: 930px;
    overflow: hidden;
    background: var(--panel-black);
    box-shadow: 0 6px 18px rgba(0,0,0,0.35);
  }
  .elements-photo {
    position: absolute;
    left: 0;
    top: 0;
    width: 764px;
    height: 930px;
    background:
      radial-gradient(circle at 78% 62%, rgba(240,110,30,0.85) 0%, rgba(160,50,20,0.55) 28%, rgba(60,20,20,0) 55%),
      radial-gradient(circle at 20% 35%, rgba(80,130,180,0.6) 0%, rgba(23,53,90,0) 45%),
      linear-gradient(135deg, var(--deep-navy) 0%, var(--water-blue) 30%, #3a2030 60%, var(--ember-red) 80%, #1a0808 100%);
  }
  .elements-photo::after {
    content: "";
    position: absolute;
    right: 0;
    top: 0;
    width: 120px;
    height: 100%;
    background: linear-gradient(90deg, rgba(0,0,0,0), var(--panel-black));
  }
  .globe {
    position: absolute;
    left: 34px;
    top: 280px;
    width: 458px;
    height: 458px;
    border-radius: 50%;
    background: radial-gradient(circle at 40% 40%, #1d3654 0%, var(--deep-navy) 70%);
    box-shadow: 18px 10px 40px rgba(240,120,30,0.6);
  }
  .headline {
    position: absolute;
    right: 72px;
    top: 52px;
    margin: 0;
    text-align: right;
    color: var(--ink-white);
    font-weight: 800;
    font-size: 68px;
    line-height: 74px;
    letter-spacing: 0.5px;
    text-shadow: 0 0 14px rgba(255,255,255,0.35);
  }
  .brand {
    position: absolute;
    left: 87px;
    top: 441px;
    display: flex;
    align-items: center;
    gap: 14px;
  }
  .brand-square {
    width: 83px;
    height: 83px;
    background: var(--ink-white);
    border-radius: 4px;
  }
  .brand-name {
    color: var(--ink-white);
    font-weight: 700;
    font-size: 62px;
    letter-spacing: 1px;
  }
  .trade {
    position: absolute;
    left: 628px;
    width: 200px;
    text-align: center;
  }
  .trade-icon {
    display: block;
    margin: 0 auto;
    width: 92px;
    height: 92px;
  }
  .trade-title {
    margin: 18px -30px 0;
    color: var(--ink-white);
    font-weight: 700;
    font-size: 20px;
    line-height: 29px;
  }
  .trade--plumbing { top: 341px; }
  .trade--electric { top: 578px; }
  .footer-band {
    position: absolute;
    left: 0;
    top: 0;
    width: 930px;
    height: 930px;
  }
  .web-address {
    position: absolute;
    left: 444px;
    top: 862px;
    width: 466px;
    text-align: center;
    color: var(--ink-white);
    font-weight: 700;
    font-size: 21px;
  }
</style>
</head>
<body>
  <div class="poster">
    <div class="elements-photo" role="img" aria-label="Wasser, Feuer und Blitze als Sinnbild für Sanitär, Heizung und Elektro">
      <div class="globe"></div>
    </div>

    <h1 class="headline">WIR BIETEN EINEN<br>AUSBILDUNG-<br>SPLÄTZE ALS</h1>

    <div class="brand">
      <div class="brand-square"></div>
      <span class="brand-name">KORVELD</span>
    </div>

    <div class="trade trade--plumbing">
      <svg class="trade-icon" viewBox="0 0 92 92" aria-hidden="true">
        <circle cx="46" cy="46" r="42" fill="none" stroke="var(--ink-white)" stroke-width="5"/>
        <g fill="none" stroke="var(--icon-yellow)" stroke-width="3" stroke-linejoin="round">
          <circle cx="46" cy="46" r="5"/>
          <path d="M46 41 C40 28 44 20 54 22 C62 24 60 34 50 42 Z"/>
          <path d="M51 47 C64 43 72 48 68 58 C64 66 56 62 50 51 Z"/>
          <path d="M44 51 C40 64 32 70 26 62 C22 54 32 50 42 49 Z"/>
          <path d="M41 45 C30 46 22 40 26 32 C30 26 38 32 42 41 Z"/>
        </g>
      </svg>
      <p class="trade-title">Anlagenmechaniker/in für Sanitär-, Heizungs- und Klimatechnik</p>
    </div>

    <div class="trade trade--electric">
      <svg class="trade-icon" viewBox="0 0 92 92" aria-hidden="true">
        <circle cx="46" cy="46" r="42" fill="none" stroke="var(--ink-white)" stroke-width="5"/>
        <g fill="none" stroke="var(--icon-yellow)" stroke-width="3" stroke-linejoin="round">
          <path d="M42 16 h8 l2 8 l7 3 l7 -5 l6 6 l-5 7 l3 7 l8 2 v8 l-8 2 l-3 7 l5 7 l-6 6 l-7 -5 l-7 3 l-2 8 h-8 l-2 -8 l-7 -3 l-7 5 l-6 -6 l5 -7 l-3 -7 l-8 -2 v-8 l8 -2 l3 -7 l-5 -7 l6 -6 l7 5 l7 -3 Z"/>
          <circle cx="46" cy="46" r="15"/>
          <path d="M48 36 l-7 11 h6 l-3 9 l8 -12 h-6 Z"/>
        </g>
      </svg>
      <p class="trade-title">Elektroinstallateur/in (Energie- und Gebäudetechnik)</p>
    </div>

    <svg class="footer-band" viewBox="0 0 930 930" aria-hidden="true">
      <path d="M0 899 H426 C455 899 462 880 475 860 C488 840 498 831 520 831 H843 C860 831 870 838 880 850 L930 912 V930 H0 Z" fill="var(--accent-red)"/>
    </svg>
    <div class="web-address">gebaeudetechnik-korveld.de</div>
  </div>
</body>
</html>
```